Design a website banner for Squarespace website

I need someone to take the image file and turn it into a banner for our website. I would also like the colours changed in our logo to match the colours of the banner.
- I will need a high resolution copy of the 2 logo designs with changed colours
- I need the colour number codes for each colour so that I can match the colours in the website accordingly.
I would like a banner without the logo and a few design variations that can be used on other pages so that the banner can vary for each page.
- Each banner will need to have white space for some basic text.

Sick

```html
<!DOCTYPE html>
<html lang="en">
<head>
<meta charset="utf-8">
<title>Website Banner</title>
<link rel="stylesheet" href="https://fonts.googleapis.com/css2?family=Montserrat:wght@500;600;700&display=swap">
<style>
  :root {
    --page-bg: #ffffff;
    --banner-bg: #ffffff;
    --accent-orange: #f39a33;
    --slate: #5c6873;
    --steel: #56656f;
    --mist-grey: #9a9c9e;
    --button-text: #ffffff;
    --edge-shadow: rgba(0, 0, 0, 0.35);
  }
  * { margin: 0; padding: 0; box-sizing: border-box; }
  html, body {
    width: 1200px;
    height: 1200px;
    overflow: hidden;
    background: var(--page-bg);
  }
  .canvas {
    position: relative;
    width: 1200px;
    height: 1200px;
  }
  .banner {
    position: absolute;
    left: 127px;
    top: 478px;
    width: 949px;
    height: 244px;
    background: var(--banner-bg);
    box-shadow: 1px 1px 2px var(--edge-shadow);
    overflow: hidden;
    font-family: "Montserrat", sans-serif;
  }
  .banner__pattern {
    position: absolute;
    inset: 0;
    width: 949px;
    height: 244px;
  }
  .banner__content {
    position: absolute;
    left: 0;
    right: 0;
    top: 66px;
    text-align: center;
  }
  .banner__title {
    color: var(--accent-orange);
    font-size: 56px;
    font-weight: 600;
    line-height: 1;
    letter-spacing: 1px;
  }
  .banner__subtitle {
    margin-top: 10px;
    color: var(--slate);
    font-size: 15px;
    font-weight: 600;
    letter-spacing: 0.3px;
  }
  .banner__link {
    display: inline-block;
    margin-top: 15px;
    width: 224px;
    height: 27px;
    line-height: 27px;
    border-radius: 14px;
    background: var(--accent-orange);
    color: var(--button-text);
    font-size: 10.5px;
    font-weight: 700;
    letter-spacing: 1px;
    text-decoration: none;
  }
</style>
</head>
<body>
  <main class="canvas">
    <section class="banner">
      <svg class="banner__pattern" viewBox="0 0 949 244" role="img" aria-label="Geometric mosaic of orange, slate and grey half-circles and hourglass shapes framing the top-right and bottom-left corners">
        <defs>
          <linearGradient id="mosaic-tone" x1="0" y1="0" x2="1" y2="1">
            <stop offset="0" stop-color="var(--accent-orange)" stop-opacity="0.75"/>
            <stop offset="0.5" stop-color="var(--mist-grey)" stop-opacity="0.7"/>
            <stop offset="1" stop-color="var(--steel)" stop-opacity="0.75"/>
          </linearGradient>
        </defs>
        <polygon class="mosaic mosaic--top-right" fill="url(#mosaic-tone)"
          points="510,0 949,0 949,220 908,220 908,108 843,108 843,66 688,66 688,42 510,42"/>
        <polygon class="mosaic mosaic--bottom-left" fill="url(#mosaic-tone)"
          points="0,145 285,145 285,220 440,220 440,244 0,244"/>
      </svg>
      <div class="banner__content">
        <h1 class="banner__title">LOREM IPSUM</h1>
        <p class="banner__subtitle">Lorem Ipsum is simply dummy text of the printing</p>
        <a class="banner__link" href="#">www.brightmindsdaily.com</a>
      </div>
    </section>
  </main>
</body>
</html>
```